Veltrix Stationary

Design the stationary of Veltrix Promotions Group.

Veltrix is a BTL company, BTL meaning "below the line". In other words Veltrix is a Promotional Marketing company (the company that design the brands promotional activities).

The design should transmit creativity, agility, boldness.

I need:
* Bis Card
* Letter head
* Envelopes, both vertical and horizontal (for legal size), and letter envelope
* Folders
* PPT template (Title page and regular page)
* CD slip (CD envelope)
* ID card (employee card)

And what ever else you want to throw in.
Updates

Guys,

Something I missed from the brief.   The predominat color should be RED.

Also, have fun and play with the exclamation mark (!) of the logo. 

Hi guys, more comments:

Remember that Veltrix is a "creativity" agency, not in the advertising side but on the promotional side, and that should reflect on the stationary.

 I want a bold design.  Bold and yet crisp.

 

Guys, i just uploaded the Logo in AI format.

I Also uploaded the actual Veltrix Bis Card, wich I like.  So I will like to see some designs with that bis card approach.

Guys, I am so sorry, but I notice in your last post that I upladed a wrong design ("13154_marketing_group_veltrix_brief225630.ai").  The problem was that I asked the designer the file in AI format and he send me thw wrong file, and since I dont have Illustrator I could not verify it.

The differences are minor, I just already ask him the correct one (similar to the EPS file).

Sorry                                   

Just post the correct AI file : "Veltrix Logo.ai"

Reason: I'm expecting more designs to choose from and also I wont be available tomorrow to decide.

Reason: Sorry guys, but we are not there yet!

Target Market(s)

Marketing directors, Marketing Managers

Industry/Entity Type

Legal

Requirements
Must have
• Must work with the logo attached.
The predominat color should be RED.
Play and have fun with the exclamation mark (!).
Should not have
• * No old fonts

Should not be:
* boring
* Informal
* rigid

```html
<!DOCTYPE html>
<html lang="en">
<head>
<meta charset="utf-8">
<title>Veltrix Promotions Group – Letterhead</title>
<link href="https://fonts.googleapis.com/css2?family=Poppins:wght@600;700&display=swap" rel="stylesheet">
<style>
  :root {
    --ink: #111111;
    --brand-red: #d0121b;
    --accent-faint: #f7d9db;
    --band-dark: #5e0509;
    --band-mid: #8e0d14;
    --band-light: #b0141d;
    --paper: #ffffff;
    --on-band: #ffffff;
  }
  * { margin: 0; padding: 0; box-sizing: border-box; }
  html, body { width: 848px; height: 1200px; overflow: hidden; background: var(--paper); }
  .letterhead {
    position: relative;
    width: 848px;
    height: 1200px;
    background: var(--paper);
    font-family: "Poppins", sans-serif;
  }
  .brand {
    position: absolute;
    left: 31px;
    top: 42px;
    display: flex;
    align-items: flex-end;
    gap: 14px;
    color: var(--ink);
    font-weight: 700;
  }
  .brand-text { display: flex; flex-direction: column; }
  .brand-name {
    font-size: 50px;
    line-height: 46px;
    letter-spacing: -1px;
  }
  .brand-tagline {
    font-size: 10.5px;
    line-height: 12px;
    letter-spacing: 4.6px;
    margin-top: 8px;
  }
  .brand-dot {
    width: 26px;
    height: 26px;
    border-radius: 50%;
    background: var(--brand-red);
    margin-bottom: 0;
  }
  .corner-accent {
    position: absolute;
    left: 718px;
    top: 132px;
    width: 64px;
    height: 64px;
    border-radius: 50%;
    background: var(--accent-faint);
  }
  .footer-band {
    position: absolute;
    left: 0;
    bottom: 0;
    width: 848px;
    height: 109px;
    background:
      radial-gradient(ellipse 60% 140% at 50% 0%, var(--band-light) 0%, var(--band-mid) 55%, var(--band-dark) 100%);
    color: var(--on-band);
    text-align: center;
    font-weight: 600;
  }
  .footer-address {
    padding-top: 27px;
    font-size: 12px;
    line-height: 15px;
  }
  .footer-phone { font-size: 12px; line-height: 15px; }
  .footer-web {
    margin-top: 5px;
    font-size: 20px;
    line-height: 26px;
    font-weight: 700;
    letter-spacing: 0.4px;
  }
</style>
</head>
<body>
  <main class="letterhead">
    <header class="brand">
      <div class="brand-text">
        <span class="brand-name">veltrix</span>
        <span class="brand-tagline">PROMOTIONS GROUP</span>
      </div>
      <span class="brand-dot"></span>
    </header>

    <span class="corner-accent" aria-hidden="true"></span>

    <footer class="footer-band">
      <p class="footer-address">Calle 18 No. 42 Ens Los Prados, Santo Domingo, Republica Dominicana</p>
      <p class="footer-phone">Tell: 809.555.0182 | Fax: 809.555.0197</p>
      <p class="footer-web">www.veltrix.com.do</p>
    </footer>
  </main>
</body>
</html>
```